Event flyer for Sunday night Youth Group

Need a 4 x 6 or 5 x 7 flyer for a new youth group starting on April 14. The youth group is for students in middle school and high school so it needs to look fun and cool, but not childish. I prefer it not to include pictures of people unless it's so obscure you can't really see their faces. I've uploaded some pictures of flyers I like. I've also attached a couple versions of our logo to use on the flyer.
Information the flyer needs to include:
Youth Group
Sundays, 6-8pm (beginning April 14)
Location: Merriwick's - 4219 Hollowfern Ln S, Keizer, 97418
There will be dinner, games, friends, and a message.
Target Market(s)
Youth ages 13-18
Industry/Entity Type
Church
Colors
Designer to choose colors to be used in the design.
Look and feel

```html
<!DOCTYPE html>
<html lang="en">
<head>
<meta charset="UTF-8">
<title>Youth Group Flyer</title>
<link rel="stylesheet" href="https://fonts.googleapis.com/css2?family=Anton&family=Oswald:wght@500;600;700&family=Yellowtail&display=swap">
<style>
  :root {
    --sky: #2fb3d6;
    --ocean: #1f5fae;
    --indigo: #2a2c7a;
    --violet: #6a2a9a;
    --orchid: #9a3fb8;
    --navy: #1a1f4d;
    --white: #ffffff;
    --yellow: #f5e63a;
    --gold: #e9c21c;
  }
  * { margin: 0; padding: 0; box-sizing: border-box; }
  html, body { width: 857px; height: 1200px; overflow: hidden; background: var(--navy); }
  .flyer {
    position: relative;
    width: 857px;
    height: 1200px;
    overflow: hidden;
    font-family: "Oswald", sans-serif;
    color: var(--white);
    text-align: center;
  }
  .backdrop {
    position: absolute; inset: 0;
    background:
      radial-gradient(ellipse 70% 40% at 20% 10%, rgba(60,200,230,.75), transparent 70%),
      radial-gradient(ellipse 60% 35% at 85% 30%, rgba(40,90,190,.7), transparent 70%),
      radial-gradient(ellipse 80% 40% at 70% 95%, rgba(170,70,200,.8), transparent 70%),
      linear-gradient(180deg, var(--sky) 0%, var(--ocean) 30%, var(--indigo) 55%, var(--violet) 80%, var(--orchid) 100%);
  }
  .brush-circle {
    position: absolute;
    left: 185px; top: 342px;
    width: 486px; height: 486px;
    border-radius: 50%;
    background: radial-gradient(circle at 45% 45%, #1d2a66 0%, var(--navy) 70%, rgba(26,31,77,.85) 100%);
  }
  .brand {
    position: absolute; top: 60px; left: 0; right: 0;
    display: flex; flex-direction: column; align-items: center;
  }
  .brand-mark {
    width: 70px; height: 70px; border-radius: 50%;
    background: var(--white);
    margin-bottom: 26px;
  }
  .brand-name {
    font-weight: 600; font-size: 40px; letter-spacing: 1px; line-height: 1.05;
    text-transform: uppercase;
  }
  .brand-name small { display: block; font-size: 22px; letter-spacing: 5px; }
  .title-script {
    position: absolute; top: 320px; left: 0; right: 0;
    font-family: "Yellowtail", cursive;
    font-size: 220px; line-height: 1;
    transform: rotate(-6deg);
  }
  .title-block {
    position: absolute; top: 535px; left: 0; right: 0;
    font-family: "Anton", sans-serif;
    font-size: 150px; line-height: 1; letter-spacing: 2px;
    color: var(--yellow);
    text-shadow: 0 4px 10px rgba(0,0,0,.35);
  }
  .schedule {
    position: absolute; top: 700px; left: 0; right: 0;
    font-weight: 600; font-size: 48px; line-height: 1.1;
  }
  .start {
    position: absolute; top: 760px; left: 0; right: 0;
    color: var(--yellow); font-weight: 600;
    font-size: 38px; line-height: 1.05;
  }
  .highlights {
    position: absolute; left: 166px; top: 905px;
    width: 525px; height: 175px;
    border: 4px solid var(--gold);
    display: flex; flex-direction: column; justify-content: center;
    font-weight: 600; line-height: 1.12;
  }
  .highlights-lead { color: var(--yellow); font-size: 46px; }
  .highlights-list { font-size: 40px; }
  .location {
    position: absolute; left: 150px; top: 1128px;
    display: flex; align-items: center; gap: 16px;
    color: var(--yellow); font-weight: 600;
    font-size: 30px; line-height: 1.1; text-align: left;
  }
  .location svg { width: 34px; height: 48px; flex: none; }
</style>
</head>
<body>
<main class="flyer">
  <div class="backdrop" role="img" aria-label="Blue to purple watercolor wash background"></div>
  <div class="brush-circle" role="img" aria-label="Dark navy brushstroke circle"></div>

  <header class="brand">
    <span class="brand-mark"></span>
    <p class="brand-name">Brightpath<small>Fellowship</small></p>
  </header>

  <h1>
    <span class="title-script">Youth</span>
    <span class="title-block">GROUP</span>
  </h1>

  <p class="schedule">SUNDAYS, 6-8PM</p>
  <p class="start">BEGINNING<br>APRIL 14</p>

  <section class="highlights">
    <p class="highlights-lead">THERE WILL BE</p>
    <p class="highlights-list">DINNER, GAMES, FRIENDS<br>AND A MESSAGE</p>
  </section>

  <p class="location">
    <svg viewBox="0 0 24 34" aria-hidden="true"><path d="M12 0C5.4 0 0 5.3 0 11.9 0 20.8 12 34 12 34s12-13.2 12-22.1C24 5.3 18.6 0 12 0zm0 17a5 5 0 1 1 0-10 5 5 0 0 1 0 10z" fill="#ffffff"/></svg>
    <span>MERRIWICK'S - 4219 HOLLOWFERN<br>LN S, KEIZER, 97418</span>
  </p>
</main>
</body>
</html>
```